Flyer-Design für Personal Training
Ich bin sehr zufrieden mit der Arbeit der Designerin. Auf Änderungswünsche wurde immer schnell eingegangen und ich habe viele tolle Inputs erhalten. Ich werde definitiv wieder mit ihr arbeiten.
Zielgruppe
Ich gebe Personal Training und Outdoor Gruppen-Training. Meine Kunden sind jung bis alt(20-50), mändlich und weiblich. Das Personal Training ist eher im Hochpreis Segment das OGT nicht.
Aufgabenstellung
Der Flyer soll die 3 athletikfaktoren: Kraft, Schnelligkeit und Ausdauer beinhalten. Farblich soll er meinem Logo angepasst sein. Der Flyer wird in Arztpraxen und Physiotherapien aufgelegt und sollte in diese Umgebung passen.
Falzflyer A6: Front Logo, inen links der Trainer und Angebot, inen rechts die beiden Trainings. Back Kontakt und map.
Ich werde die Flyer bei Druckmalo drucken lassen - bitte die druckvorlagen beachten (seitenränder usw.)
Im pdf Flyer sind die Texte.
Bitte einen QR für Zulo und ev. noch einen für die Kontaktdaten in das Layout einbauen.

```html
<!DOCTYPE html>
<html lang="de">
<head>
<meta charset="utf-8">
<title>Kraft &amp; Balance – Flyer</title>
<link rel="stylesheet" href="https://fonts.googleapis.com/css2?family=Jura:wght@500;600&family=Arimo:wght@400&display=swap">
<style>
  :root {
    --navy: #173a72;
    --blue: #1f72bd;
    --sky: #4eb2e1;
    --pale: #93bfe6;
    --mist: #c4dcf6;
    --ground: #e4e3e5;
    --white: #ffffff;
    --ink: #1d3466;
  }
  * { margin: 0; padding: 0; box-sizing: border-box; }
  html, body { width: 785px; height: 1200px; overflow: hidden; background: var(--ground); }
  body { position: relative; font-family: "Arimo", Arial, sans-serif; }

  .sheet { position: absolute; background: var(--white); overflow: hidden; }
  .sheet--outer { left: 24px; top: 48px; width: 737px; height: 527px; }
  .sheet--inner { left: 23px; top: 610px; width: 740px; height: 528px; }

  .deco { position: absolute; left: 0; top: 0; }
  .photo, .map {
    position: absolute; border-radius: 50%;
  }
  .photo--hero {
    left: 0; top: 0; width: 737px; height: 435px; border-radius: 0;
    background: radial-gradient(ellipse at 35% 65%, #5b5d60 0%, #2e3033 45%, #1b1c1e 100%);
  }
  .map {
    left: 13px; top: 18px; width: 202px; height: 202px;
    background: linear-gradient(135deg, #e9eef0 0%, #f4f5f1 55%, #cfe8cf 100%);
    border: 6px solid var(--blue);
  }

  .badge {
    position: absolute; border-radius: 50%; background: var(--navy);
    display: flex; align-items: center; justify-content: center; text-align: center;
    color: var(--white); font-family: "Jura", sans-serif; font-weight: 600;
    letter-spacing: 0.08em; line-height: 1.2;
  }
  .badge--large { left: 383px; top: -7px; width: 170px; height: 170px; font-size: 12px; }
  .badge--small { width: 62px; height: 62px; font-size: 5.5px; }
  .badge--medium { width: 78px; height: 78px; font-size: 7px; }

  .band { position: absolute; left: 0; width: 100%; }
  .band--accent { top: 435px; height: 56px; background: var(--blue); }
  .band--contact { background: var(--navy); }
  .sheet--outer .band--contact { top: 491px; height: 36px; }
  .sheet--inner .band--stripe { top: 483px; height: 10px; background: var(--blue); }
  .sheet--inner .band--contact { top: 493px; height: 35px; }

  .slogan {
    position: absolute; top: 22px; left: 0; width: 384px; text-align: center;
    color: var(--white); font-family: "Jura", sans-serif; font-weight: 600; font-size: 21px;
    letter-spacing: 0.02em;
  }
  .offer-title {
    position: absolute; top: 5px; left: 395px; width: 330px; text-align: center;
    color: var(--white); font-family: "Jura", sans-serif; font-weight: 500; font-size: 21.5px;
    line-height: 1.02; letter-spacing: 0.02em;
  }

  .contact-item {
    position: absolute; top: 50%; transform: translateY(-50%);
    color: var(--white); font-size: 6.4px; line-height: 1.15; display: flex; align-items: center; gap: 4px;
  }
  .contact-sep { position: absolute; top: 6px; width: 1px; height: 22px; background: var(--white); }
  .social-box { width: 9px; height: 9px; border: 1px solid var(--white); border-radius: 2px; }

  .heading {
    position: absolute; color: var(--ink); font-family: "Jura", sans-serif; font-weight: 600;
  }
  .copy { position: absolute; color: var(--ink); font-size: 10.2px; line-height: 12px; }

  .who-heading { left: 20px; top: 285px; font-size: 13px; }
  .who-copy { left: 20px; top: 311px; width: 345px; }
  .offer-heading { left: 19px; top: 395px; font-size: 13px; }
  .offer-list { position: absolute; left: 70px; top: 418px; width: 260px; list-style: none; display: grid; grid-template-columns: 146px 114px; row-gap: 10px; }
  .offer-list li { display: flex; align-items: center; gap: 7px; color: var(--navy); font-family: "Jura", sans-serif; font-weight: 600; font-size: 10px; }
  .tick { width: 17px; height: 17px; flex: none; }

  .group-heading { left: 384px; top: 36px; font-size: 12.5px; }
  .group-copy { left: 384px; top: 67px; width: 175px; }
  .pt-heading { right: 34px; top: 264px; font-size: 12.5px; }
  .pt-copy { right: 34px; top: 293px; width: 140px; text-align: right; }
</style>
</head>
<body>

<section class="sheet sheet--outer" aria-label="Flyer Außenseite">
  <div class="photo photo--hero" role="img" aria-label="Foto: Kurzhanteln im Ablagegestell eines Fitnessstudios"></div>

  <svg class="deco" width="737" height="435" viewBox="0 0 737 435" aria-hidden="true">
    <circle cx="565" cy="207" r="180" fill="#2f83d0" fill-opacity="0.55"/>
    <circle cx="585" cy="171" r="105" fill="#6fb0ea" fill-opacity="0.35"/>
    <circle cx="624" cy="178" r="134" fill="none" stroke="#3fb0ea" stroke-width="1"/>
    <circle cx="590" cy="190" r="172" fill="none" stroke="#3fb0ea" stroke-width="0.8"/>
    <circle cx="437" cy="214" r="59" fill="#4eb2e1" fill-opacity="0.5"/>
    <circle cx="465" cy="322" r="21" fill="#1f72bd"/>
  </svg>

  <div class="map" role="img" aria-label="Stadtplan mit Standort des Trainingsstudios"></div>
  <div class="badge badge--small" style="left:143px; top:157px;">KRAFT &amp; BALANCE</div>
  <div class="badge badge--large">KRAFT &amp; BALANCE</div>

  <div class="band band--accent">
    <p class="slogan">START TRAINING TODAY!!!</p>
    <p class="offer-title">Personal Training &amp;<br>Outdoor Gruppen-Training</p>
  </div>

  <div class="band band--contact">
    <span class="contact-item" style="left:37px;">Tel: +49 1520 447 61</span>
    <span class="contact-sep" style="left:153px;"></span>
    <span class="contact-item" style="left:158px;">E-mail: info@welbrick-fit.de<br>www.welbrick-fit.de</span>
    <span class="contact-sep" style="left:268px;"></span>
    <span class="contact-item" style="left:272px;"><span class="social-box"></span>welbrick_fit</span>
    <span class="contact-sep" style="left:392px;"></span>
    <span class="contact-item" style="left:398px;">Birkenweg 3<br>D-66100 Feldheim</span>
    <span class="contact-sep" style="left:514px;"></span>
    <span class="contact-item" style="left:520px;">Tel: +49 1520 447 61<br>E-mail: info@welbrick-fit.de</span>
    <span class="contact-sep" style="left:630px;"></span>
    <span class="contact-item" style="left:635px;">Tel: +49 1520 447 61<br>E-mail: info@welbrick-fit.de</span>
  </div>
</section>

<section class="sheet sheet--inner" aria-label="Flyer Innenseite">
  <svg class="deco" width="740" height="528" viewBox="0 0 740 528" aria-hidden="true">
    <circle cx="224" cy="143" r="146" fill="none" stroke="#2aa3e3" stroke-width="1"/>
    <circle cx="235" cy="133" r="134" fill="#93bfe6"/>
    <circle cx="46" cy="43" r="13" fill="#1f72bd"/>
    <circle cx="164" cy="272" r="7" fill="#1f72bd"/>
    <circle cx="515" cy="158" r="14" fill="#1f72bd"/>
    <circle cx="474" cy="280" r="97" fill="none" stroke="#2aa3e3" stroke-width="1"/>
    <circle cx="614" cy="426" r="7" fill="#1f72bd"/>
  </svg>

  <div class="photo" style="left:140px; top:12px; width:212px; height:212px; background: radial-gradient(circle at 50% 55%, #d9dbde 0%, #b9bcc0 100%);" role="img" aria-label="Porträtfoto des Trainers"></div>
  <div class="photo" style="left:632px; top:43px; width:0; height:0;"></div>
  <div class="photo" style="left:547px; top:43px; width:170px; height:170px; background: linear-gradient(180deg, #7f9b78 0%, #5f7e5a 45%, #8fa19a 60%, #7a8a86 100%);" role="img" aria-label="Foto: Outdoor-Gruppentraining auf dem Sportplatz"></div>
  <div class="photo" style="left:382px; top:188px; width:184px; height:184px; background: linear-gradient(180deg, #eceeef 0%, #d7dadc 55%, #4a4d52 75%, #3a3c40 100%);" role="img" aria-label="Foto: privates Fitnessstudio mit Hantelrack"></div>

  <svg class="deco" width="740" height="528" viewBox="0 0 740 528" aria-hidden="true">
    <circle cx="156" cy="67" r="38" fill="#4eb2e1" fill-opacity="0.55"/>
    <circle cx="306" cy="240" r="56" fill="#a9cdf6" fill-opacity="0.8"/>
    <circle cx="566" cy="58" r="37" fill="#4eb2e1" fill-opacity="0.6"/>
    <circle cx="440" cy="389" r="56" fill="#c4dcf6"/>
    <circle cx="592" cy="310" r="33" fill="#4eb2e1" fill-opacity="0.6"/>
  </svg>

  <div class="badge badge--medium" style="left:18px; top:192px;">KRAFT &amp; BALANCE</div>
  <div class="badge badge--medium" style="left:630px; top:410px;">KRAFT &amp; BALANCE</div>

  <h2 class="heading who-heading">Wer bin ich:</h2>
  <p class="copy who-copy">Als ehemaliger Leistungssportler in der Leichtathletik und später im Kickboxen habe ich selbst über 20 Jahre an meiner Kraft, Schnelligkeit und Ausdauer gearbeitet. Als Trainer kann ich nun meine Erfahrungen an Dich weitergeben. Zahlreiche Aus- und Weiterbildungen im Personal Training, Functional Training und im Outdoor Training ermöglichen es mir, Dich professionell zu deinem Ziel zu führen.</p>

  <h2 class="heading offer-heading">Angebot:</h2>
  <ul class="offer-list">
    <li><svg class="tick" viewBox="0 0 17 17"><circle cx="8" cy="9.5" r="7" fill="#c4dcf6"/><path d="M3 8 L7 12 L15 2" fill="none" stroke="#173a72" stroke-width="2.6"/></svg>Personal Training</li>
    <li><svg class="tick" viewBox="0 0 17 17"><circle cx="8" cy="9.5" r="7" fill="#c4dcf6"/><path d="M3 8 L7 12 L15 2" fill="none" stroke="#173a72" stroke-width="2.6"/></svg>Athletik Training</li>
    <li><svg class="tick" viewBox="0 0 17 17"><circle cx="8" cy="9.5" r="7" fill="#c4dcf6"/><path d="M3 8 L7 12 L15 2" fill="none" stroke="#173a72" stroke-width="2.6"/></svg>Personal Training Duo</li>
    <li><svg class="tick" viewBox="0 0 17 17"><circle cx="8" cy="9.5" r="7" fill="#c4dcf6"/><path d="M3 8 L7 12 L15 2" fill="none" stroke="#173a72" stroke-width="2.6"/></svg>Outdoor Training</li>
  </ul>

  <h2 class="heading group-heading">Outdoor Gruppen – Training:</h2>
  <p class="copy group-copy">Training im Freien mit dem eigenen Körpergewicht mit verschiedenen hilfsmitteln in Gruppen mit max. 10 Teilnehmenden, für Einsteigerinnen bis Fortgeschrittene.</p>

  <h2 class="heading pt-heading">Personal Training:</h2>
  <p class="copy pt-copy">Nach Analyse deiner Fitness/Leistungsfähigkeit erstelle ich einen individuell auf dich abgestimmten Trainingsplan und betreue dich 1:1 in meinem privaten Fitnessstudio, im Freien oder bei dir zuhause.</p>

  <div class="band band--stripe"></div>
  <div class="band band--contact">
    <span class="contact-sep" style="left:26px;"></span>
    <span class="contact-item" style="left:31px;">Tel: +49 1520 447 61</span>
    <span class="contact-sep" style="left:147px;"></span>
    <span class="contact-item" style="left:151px;">E-mail: info@welbrick-fit.de<br>www.welbrick-fit.de</span>
    <span class="contact-sep" style="left:263px;"></span>
    <span class="contact-item" style="left:266px;"><span class="social-box"></span>welbrick_fit</span>
    <span class="contact-sep" style="left:384px;"></span>
    <span class="contact-item" style="left:388px;">Tel: +49 1520 447 61</span>
    <span class="contact-sep" style="left:506px;"></span>
    <span class="contact-item" style="left:510px;">E-mail: info@welbrick-fit.de<br>www.welbrick-fit.de</span>
    <span class="contact-sep" style="left:622px;"></span>
    <span class="contact-item" style="left:625px;"><span class="social-box"></span>welbrick_fit</span>
  </div>
</section>

</body>
</html>
```